Business Card for Auto Dealership - Clean, sharp and professional

Please use the maroon logo with the grey background. Need a sharp, clean and professional business card for an Auto Dealer. In the files provides there is three different logos. I have not decided which one to go with yet. Right now I am favoring the grey/silver background. I would like my contact info on there and the website as well. I feel like less is more and want something simple, clean and sharp. Thank you in advance for your tie and effort! I also need email signature, letterhead, etc after this

Target Market(s)

Car buyers

Industry/Entity Type

Automotive

Contact Information for Business Card

Dean
555-417-2386
www.BrinwoodAutoHub.example
Dean@BrinwoodAutoHub.example

Font styles to use
Serif
Sans Serif

Requirements
Must have
• Please use the maroon logo with the grey background. Business Card Details and logo from files. Please stick to the logo colors

```html
<!DOCTYPE html>
<html lang="en">
<head>
<meta charset="utf-8">
<title>Brinwood Auto Hub – Business Card</title>
<link href="https://fonts.googleapis.com/css2?family=Arimo:wght@400;700&display=swap" rel="stylesheet">
<style>
  :root {
    --maroon: #4a1616;
    --panel: #ebebed;
    --white: #ffffff;
    --backdrop: #dcdad8;
  }
  * { margin: 0; padding: 0; box-sizing: border-box; }
  html, body { width: 1200px; height: 1200px; overflow: hidden; }
  body {
    background: var(--backdrop);
    font-family: "Arimo", Arial, sans-serif;
    display: flex;
    flex-direction: column;
    align-items: center;
    justify-content: center;
    gap: 60px;
  }
  .card {
    width: 860px;
    height: 491px;
    position: relative;
    background: var(--maroon);
    box-shadow: 0 10px 30px rgba(0,0,0,.25);
    overflow: hidden;
  }
  /* Contact side */
  .contact-side .brand-mark {
    position: absolute;
    left: 70px;
    top: 250px;
    display: flex;
    align-items: center;
    gap: 16px;
    color: var(--white);
  }
  .brand-mark .dot {
    width: 110px; height: 110px;
    border: 8px solid var(--white);
    border-radius: 50%;
  }
  .brand-mark .name {
    font-weight: 700;
    font-size: 22px;
    letter-spacing: 1px;
    text-transform: uppercase;
    width: 120px;
    line-height: 1.2;
  }
  .contact-block {
    position: absolute;
    left: 395px;
    top: 125px;
    color: var(--white);
  }
  .contact-block .person {
    font-size: 36px;
    margin-bottom: 14px;
    margin-left: 2px;
  }
  .contact-block .line {
    display: flex;
    align-items: center;
    gap: 14px;
    font-size: 25px;
    margin-bottom: 12px;
  }
  .icon { width: 26px; height: 26px; flex: none; }
  /* Logo side */
  .logo-side svg.frame { position: absolute; inset: 0; }
  .logo-lockup {
    position: absolute;
    left: 190px;
    top: 178px;
    display: flex;
    align-items: center;
    gap: 26px;
    color: var(--maroon);
  }
  .logo-lockup .dot {
    width: 130px; height: 130px;
    border: 12px solid var(--maroon);
    border-radius: 50%;
  }
  .logo-lockup .wordmark {
    font-weight: 700;
    line-height: 1;
    text-transform: uppercase;
  }
  .wordmark .primary { font-size: 62px; letter-spacing: 2px; display: block; }
  .wordmark .secondary { font-size: 22px; letter-spacing: 15px; display: block; margin-top: 8px; }
</style>
</head>
<body>
  <section class="card contact-side">
    <div class="brand-mark">
      <div class="dot"></div>
      <div class="name">Brinwood Auto Hub</div>
    </div>
    <div class="contact-block">
      <p class="person">Dean</p>
      <p class="line">
        <svg class="icon" viewBox="0 0 26 26"><circle cx="13" cy="13" r="13" fill="#fff"/><path d="M9 7l3 0 1 4-2 1a8 8 0 0 0 4 4l1-2 4 1 0 3c-6 1-12-5-11-11z" fill="#4a1616"/></svg>
        555-417-2386
      </p>
      <p class="line">
        <svg class="icon" viewBox="0 0 26 26"><circle cx="13" cy="13" r="13" fill="#fff"/><circle cx="13" cy="13" r="7" fill="none" stroke="#4a1616" stroke-width="2"/><ellipse cx="13" cy="13" rx="3" ry="7" fill="none" stroke="#4a1616" stroke-width="1.6"/><line x1="6" y1="13" x2="20" y2="13" stroke="#4a1616" stroke-width="1.6"/></svg>
        www.BrinwoodAutoHub.example
      </p>
      <p class="line">
        <svg class="icon" viewBox="0 0 26 26"><circle cx="13" cy="13" r="13" fill="#fff"/><rect x="6.5" y="8.5" width="13" height="9" fill="#4a1616"/><path d="M6.5 8.5l6.5 5 6.5-5" fill="none" stroke="#fff" stroke-width="1.4"/></svg>
        Dean@BrinwoodAutoHub.example
      </p>
    </div>
  </section>

  <section class="card logo-side">
    <svg class="frame" viewBox="0 0 860 491" aria-hidden="true">
      <path d="M210,14 H650 V44 H700 Q772,44 772,120 V371 Q772,447 700,447 H650 V477 H210 V447 H160 Q88,447 88,371 V120 Q88,44 160,44 H210 Z"
            fill="none" stroke="#fff" stroke-width="4"/>
      <path transform="translate(430 245.5) scale(0.955) translate(-430 -245.5)"
            d="M210,14 H650 V44 H700 Q772,44 772,120 V371 Q772,447 700,447 H650 V477 H210 V447 H160 Q88,447 88,371 V120 Q88,44 160,44 H210 Z"
            fill="#ebebed"/>
    </svg>
    <div class="logo-lockup">
      <div class="dot"></div>
      <div class="wordmark">
        <span class="primary">Brinwood</span>
        <span class="secondary">Auto Hub</span>
      </div>
    </div>
  </section>
</body>
</html>
```